Website Design

Hi I would like to invite designers to re design my website .

I would like the below in brief.

On the Welcome Page.

A nice looking technical page distributed into two

SALES on one side and TECHNOLOGY on the other . once the person clicks on either of them they can explore the pages in detail.

I am keen and almost ready with information for the Technology page and would like this to begin kicking ASAP .

my current website is www.brimvoltek.net

Looking forward to seeing your feedback!

Tobiah
Updates

Hi,

 
A little more elaboration on the web front page . I need it to be more techy .

I was looking at a wheel on the Technical side or a spanner and screew driver done on flash .

Just to give you a better idea on what seperated Sales from Technology. 

Computing, Storage , Components , Peripherals , Software , TV & Gaming / Entertainment , Home & Leisure , Software , Gift Vouchers , Phones etc.

Technology .

Solar Power Solutions , Security Systems , Access Control , Automatic Gates & Turnstiles , Home/Office/Hotel Automation, Indoor and Outdoor PABX Telephony, Networking , Electricity Power Meters , IP Based Technology and ETC. 

See attached on the project updates my business card design if it can give you an idea ,also see revised Logo

```html
<!DOCTYPE html>
<html lang="en">
<head>
<meta charset="utf-8">
<title>Brimvoltek — Home</title>
<link href="https://fonts.googleapis.com/css2?family=Arimo:wght@400;700&family=Oswald:wght@600&display=swap" rel="stylesheet">
<style>
  :root {
    --bg-top: #5a5a5a;
    --bg-mid: #2e2e2e;
    --bg-bottom: #151515;
    --nav-red: #d21a0c;
    --nav-red-dark: #b81408;
    --nav-active: #2a2a2a;
    --nav-divider: #e85a4f;
    --text-light: #ffffff;
    --text-muted: #cfcfcf;
    --brand-red: #d8160a;
    --dial-top: #c9c9c9;
    --dial-bottom: #efefef;
    --dial-face: #ffffff;
    --dial-title: #555555;
    --icon-dark: #2b2b2b;
    --rule: #d8d8d8;
    --social-fill: #3a3a3a;
    --social-ring: #8a8a8a;
  }
  * { margin: 0; padding: 0; box-sizing: border-box; }
  html, body { width: 1200px; height: 675px; overflow: hidden; }
  body {
    position: relative;
    font-family: "Arimo", Arial, sans-serif;
    background:
      repeating-linear-gradient(90deg, rgba(255,255,255,0.025) 0 1px, rgba(0,0,0,0.04) 1px 3px, rgba(255,255,255,0.015) 3px 4px),
      linear-gradient(180deg, var(--bg-top) 0%, var(--bg-mid) 45%, var(--bg-bottom) 100%);
  }
  .brand {
    position: absolute; left: 0; width: 1200px; top: 40px;
    text-align: center;
    font-family: "Arimo", Arial, sans-serif;
    font-weight: 700; font-size: 44px; letter-spacing: 1px;
    color: var(--brand-red);
  }
  .main-nav {
    position: absolute; left: 161px; top: 137px; width: 878px; height: 32px;
    background: linear-gradient(180deg, var(--nav-red) 0%, var(--nav-red-dark) 100%);
    border-radius: 4px;
    box-shadow: 0 8px 10px -4px rgba(0,0,0,0.6);
  }
  .main-nav ul { list-style: none; position: absolute; left: 201px; top: 0; height: 32px; display: flex; }
  .main-nav li {
    height: 32px; line-height: 32px; padding: 0 24px;
    font-size: 13px; color: var(--text-light);
    border-right: 1px solid var(--nav-divider);
  }
  .main-nav li:last-child { border-right: none; }
  .main-nav li.active { background: var(--nav-active); border-right: none; }
  .dial {
    position: absolute; top: 229px; width: 224px; height: 224px; border-radius: 50%;
    background: linear-gradient(180deg, var(--dial-top) 50%, var(--dial-bottom) 50%);
    box-shadow: 6px 14px 18px rgba(0,0,0,0.55);
  }
  .dial-sales { left: 339px; }
  .dial-tech { left: 638px; }
  .dial-face {
    position: absolute; left: 14px; top: 6px; width: 196px; height: 212px; border-radius: 50%;
    background: var(--dial-face);
  }
  .dial-title {
    position: absolute; left: 0; right: 0; top: 50px; text-align: center;
    font-family: "Oswald", "Arial Narrow", sans-serif; font-weight: 600;
    font-size: 21px; color: var(--dial-title); letter-spacing: -0.5px;
  }
  .dial-icon { position: absolute; left: 64px; top: 92px; width: 80px; height: 72px; }
  .footer-rule { position: absolute; left: 161px; top: 530px; width: 878px; height: 1px; background: var(--rule); }
  .footer-note {
    position: absolute; left: 0; width: 1200px; top: 570px; text-align: center;
    font-size: 12px; color: var(--text-muted);
  }
  .footer-note .sep { margin: 0 12px; }
  .social { position: absolute; left: 545px; top: 610px; display: flex; gap: 10px; }
  .social span {
    width: 30px; height: 30px; border-radius: 50%;
    background: var(--social-fill); border: 2px solid var(--social-ring);
    box-shadow: 0 1px 3px rgba(0,0,0,0.7);
  }
</style>
</head>
<body>
  <header class="brand">Brimvoltek</header>

  <nav class="main-nav">
    <ul>
      <li class="active">HOME</li>
      <li>ABOUT</li>
      <li>SALES</li>
      <li>TECHNOLOGY</li>
      <li>CONTACT</li>
    </ul>
  </nav>

  <section class="dial dial-sales">
    <div class="dial-face">
      <h2 class="dial-title">SALES</h2>
      <svg class="dial-icon" viewBox="0 0 80 72" aria-hidden="true">
        <path d="M28 8 h24 a4 4 0 0 1 4 4 v6 h-6 v-4 h-20 v4 h-6 v-6 a4 4 0 0 1 4 -4z" fill="var(--icon-dark)"/>
        <path d="M6 20 h68 a4 4 0 0 1 4 4 v10 q-38 12 -76 0 v-10 a4 4 0 0 1 4 -4z" fill="var(--icon-dark)"/>
        <path d="M6 40 q34 10 68 0 v24 a4 4 0 0 1 -4 4 h-60 a4 4 0 0 1 -4 -4z" fill="var(--icon-dark)"/>
        <rect x="34" y="36" width="12" height="10" rx="2" fill="var(--dial-face)"/>
      </svg>
    </div>
  </section>

  <section class="dial dial-tech">
    <div class="dial-face">
      <h2 class="dial-title">TECHNOLOGY</h2>
      <svg class="dial-icon" viewBox="0 0 80 72" aria-hidden="true">
        <path d="M62 2 l6 4 -16 22 -4 -3z" fill="var(--icon-dark)"/>
        <path d="M50 24 l5 4 -34 38 a5 5 0 0 1 -8 -6z" fill="var(--icon-dark)"/>
        <path d="M12 4 a14 14 0 0 0 -4 20 a14 14 0 0 0 14 4 l38 38 a5 5 0 0 0 8 -7 l-38 -38 a14 14 0 0 0 -4 -14 a14 14 0 0 0 -12 -4 l8 8 -2 7 -7 2 -8 -8z" fill="var(--icon-dark)"/>
      </svg>
    </div>
  </section>

  <div class="footer-rule"></div>
  <footer class="footer-note">Copyright © Brimvoltek 2013<span class="sep">I</span>Terms &amp; Conditions</footer>
  <div class="social" aria-label="Social links">
    <span></span><span></span><span></span>
  </div>
</body>
</html>
```